New to CraftHive? This Contest is for you!

Are you new to CraftHive and looking to enter your first contest? Look no further! We're launching this special contest to help you get started on building a design portfolio at CraftHive!

Requirements:
* Create ONE beautiful and eye-catching graphic design which includes the words "Find me on CraftHive!"

* Yes, designers are limited to 1 design submission, so show us your best work!

* Upload your design to this contest AND upload it on your Chatterbook, tagging @CraftHive and add your designer portfolio url to the description.

* You must upload your entry before 12:00am 1 June AEST

* This must be your very FIRST entry on CraftHive to be eligible to receive a prize. If you've already entered other CraftHive contests you won't be eligible to win the prizes.

* Your design must adhere to our quality standards to be eligible to receive a prize.

Prizes:
* There are 150 x $5 participation payments ($750) available to be awarded to high-quality designs
* First prize for the best design is $150
* Second prize is $100

Target Market(s)

CraftHive customers
CraftHive team of design pros.

Requirements
Must have
• Your name or name on CraftHive and the words "Find me on CraftHive".
• Create a graphic that expresses your personal design aesthetic. Option to mention your design services.
• You need to set your own art direction and carefully combine elements like
• Color, layout, typography and other elements to create a striking visual design that will catch the judging panel's eyes.
• 1200*1000 px (the standard maximum size to upload a preview image on CraftHive).
• 1 design per designer
Should not have
• Don't use the CraftHive corporate font or recycle our logo or branding - this project is all about promoting your personal graphic design style.

```html
<!DOCTYPE html>
<html lang="en">
<head>
<meta charset="utf-8">
<title>Find me on CraftHive</title>
<link rel="stylesheet" href="https://fonts.googleapis.com/css2?family=Rubik+Wet+Paint&display=swap">
<style>
  :root {
    --brick-light: #dcbd6a;
    --brick-mid: #b9984a;
    --slime-green: #38ff1e;
    --outline-white: #ffffff;
    --shadow-black: #111111;
    --brand-orange: #f0641c;
    --zombie-green: #9fd8b0;
    --zombie-flesh: #e9cf9c;
    --zombie-red: #d9563a;
    --zombie-hair: #5a3424;
    --void-black: #141414;
  }
  html, body {
    margin: 0;
    padding: 0;
    width: 1200px;
    height: 1000px;
    overflow: hidden;
    background: var(--brick-light);
  }
  .poster {
    position: relative;
    width: 1200px;
    height: 1000px;
    overflow: hidden;
  }
  .brick-wall {
    position: absolute;
    inset: 0;
    background:
      radial-gradient(ellipse at 20% 85%, rgba(60,60,40,.55), transparent 45%),
      radial-gradient(ellipse at 10% 20%, rgba(80,80,60,.35), transparent 40%),
      radial-gradient(ellipse at 75% 20%, rgba(255,240,200,.35), transparent 50%),
      linear-gradient(160deg, var(--brick-light), var(--brick-mid));
  }
  .zombie-illustration {
    position: absolute;
    left: 540px;
    top: 130px;
    width: 660px;
    height: 870px;
    border-radius: 220px 220px 0 0;
    background: linear-gradient(180deg,
      var(--zombie-hair) 0%,
      var(--zombie-green) 28%,
      var(--zombie-red) 55%,
      var(--zombie-flesh) 72%,
      var(--void-black) 88%);
  }
  .headline {
    position: absolute;
    left: 30px;
    top: 10px;
    width: 560px;
    margin: 0;
    font-family: "Rubik Wet Paint", system-ui, sans-serif;
    font-weight: 400;
    color: var(--slime-green);
    line-height: .8;
    -webkit-text-stroke: 4px var(--outline-white);
    paint-order: stroke fill;
    text-shadow: 8px 8px 0 var(--shadow-black);
  }
  .headline span {
    display: block;
    transform-origin: left top;
  }
  .headline .word-find { font-size: 300px; transform: scaleX(.62); }
  .headline .word-me   { font-size: 230px; margin-left: 95px; margin-top: 10px; transform: scaleX(.72); }
  .headline .word-on   { font-size: 240px; margin-left: 125px; margin-top: 20px; transform: scaleX(.68); }
  .brand-name {
    position: absolute;
    right: 40px;
    top: 30px;
    margin: 0;
    font-family: "Rubik Wet Paint", system-ui, sans-serif;
    font-size: 78px;
    line-height: 1;
    color: var(--brand-orange);
    letter-spacing: 2px;
  }
</style>
</head>
<body>
  <main class="poster">
    <div class="brick-wall" role="img" aria-label="Weathered yellow brick wall texture"></div>

    <div class="zombie-illustration" role="img"
         aria-label="Illustrated nerdy zombie with glasses, exposed brain and suspenders, raising one finger as he climbs out of a torn black hole in the wall"></div>

    <h1 class="headline" aria-label="Find me on">
      <span class="word-find">FIND</span>
      <span class="word-me">ME</span>
      <span class="word-on">ON</span>
    </h1>

    <p class="brand-name">CraftHive</p>
  </main>
</body>
</html>
```